Design website home page for pathology consulting company

Starting a new consulting company with anatomic pathologists focused on expert diagnosis and second opinions on difficult pathology cases. In the near future we will be incorporating next generation diagnostics for rare diseases of childhood into the business. These include discovery and testing of DNA for mutations.

The company is formed around one of the best known pathologists in the world named Marcus "Buddy" Halvorsen. The name of the company is "BuddyScope"

We had a logo design by Sketchfold - it is great. I will attach file as soon as I have it (contest ending today). Our company is medical, uses microscopes, DNA, probably will focus on childhood diseases but not solely on childhood diseases. we're not particularly conservative, but the customers we want to appeal to include older practicing pathologists as well as patients (sometimes parents) looking for second opinions.

Think a group of expert doctors diagnosing disease through the microscope and through DNA technology, ages ranging from 35-75 all trained by the best pathologist in the world - "Buddy"

We receive glass slides from diseases from patients all over the world from docs who need an expert to tell them what is the diagnosis. So "path to the diagnosis" is also part of the company marketing message.

We want the website design to describe our company but be very simple to find what one is looking for as we will use it as the launch page to:
1) order services
2) check results/reports
3) set up new account
4) speak with one of the pathologists
5) see our test menu
6) access our educational material/webinars

Update - looking for home page design and then finalists will ask for second page design to keep with theme - ok?

Reason: realized this project isn't web design but web home page design - thanks

Reason: Holidays for some in next two weeks

Reason: Hot discussion among collaborators for a few of the submissions. Will provide detail individually this weekend. Thanks so much for all the submissions!

Target Market(s)

Referring pathologists, physicians who want second opinions on pathology disease diagnosis, patients who have had biopsies (either patients themselves or parents of patients), generally high education level

Industry/Entity Type

Marketing

Requirements
Must have
• BuddyScope
Next Generation Pathology Consultants

```html
<!DOCTYPE html>
<html lang="en">
<head>
<meta charset="utf-8">
<title>BuddyScope — Next Generation Pathology Consultants</title>
<link href="https://fonts.googleapis.com/css2?family=Roboto:wght@300;400;500;700&family=Bree+Serif&display=swap" rel="stylesheet">
<style>
:root{
  --page:#ececec;
  --card:#f6f6f6;
  --card-edge:#ffffff;
  --blue:#0b66b2;
  --blue-deep:#07589c;
  --blue-bright:#1a82d4;
  --ink:#555555;
  --ink-soft:#666666;
  --date:#8a8a8a;
  --rule:#dcdcdc;
  --sky-top:#8ccbe8;
  --sky-bottom:#d9eef8;
}
*{box-sizing:border-box;margin:0;padding:0}
html,body{width:1164px;height:1200px;overflow:hidden}
body{background:var(--page);font-family:'Roboto',sans-serif;color:var(--ink);position:relative}
a{color:inherit;text-decoration:none}
.abs{position:absolute}

/* header */
.brand{left:130px;top:14px;width:200px;text-align:center}
.brand-dot{width:74px;height:74px;border-radius:50%;background:#9aa3ad;margin:0 auto 8px}
.brand-name{font-size:28px;font-weight:500;color:var(--blue);letter-spacing:.5px;line-height:1}
.brand-tag{font-size:11px;color:#777;margin-top:4px}
.account-links{right:130px;top:4px;font-size:12.5px;color:var(--blue)}
.account-links span{color:#bbb;margin:0 4px}
.phone{right:128px;top:44px;display:flex;align-items:center;gap:9px;font-size:20px;font-weight:500;color:var(--blue)}
.cta-order{left:438px;top:91px;width:122px;height:36px;background:var(--blue-bright);color:#fff;font-size:14px;font-weight:500;display:flex;align-items:center;justify-content:center;border-radius:4px;transform:skewX(-6deg);box-shadow:0 2px 3px rgba(0,0,0,.2)}
.cta-order span{transform:skewX(6deg)}
.main-nav{right:130px;font-size:14px;font-weight:500;color:#555;white-space:nowrap}
.main-nav i{font-style:normal;color:#999;margin:0 5px;font-weight:300}
.nav-row1{top:99px}
.nav-row2{top:127px}

/* hero */
.hero{left:0;top:160px;width:1164px;height:382px;background:linear-gradient(180deg,var(--sky-top) 0%,#b5ddf0 55%,var(--sky-bottom) 100%)}
.hero-panel{left:132px;top:160px;width:256px;height:382px;background:linear-gradient(180deg,rgba(8,96,172,.95) 0%,rgba(30,120,190,.75) 60%,rgba(120,190,230,.35) 100%)}
.hero-title{left:170px;top:188px;font-family:'Bree Serif',serif;font-size:40px;line-height:55px;color:#fff;text-shadow:0 2px 3px rgba(0,0,0,.35)}
.hero-arrow{top:330px}

/* cards */
.card{background:var(--card);border:2px solid var(--card-edge);box-shadow:0 1px 3px rgba(0,0,0,.12)}
.btn{display:inline-flex;align-items:center;gap:6px;background:var(--blue-bright);color:#fff;font-size:14.5px;font-weight:500;height:28px;padding:0 10px;border-radius:3px;border:1px solid var(--blue-deep)}
.news{left:128px;top:575px;width:218px;height:432px}
.news-head{position:absolute;left:-1px;top:0;width:218px;height:36px;background:linear-gradient(180deg,#1c86d6,var(--blue));color:#fff;font-size:19px;padding:6px 17px;border-radius:3px 3px 0 0}
.news-item{position:absolute;left:19px;width:182px}
.news-item h3{font-size:14.5px;font-weight:400;color:#555}
.news-date{display:inline-block;background:#8a8a8a;color:#fff;font-size:12px;padding:3px 16px;width:100px;margin:8px 0 10px}
.news-item p{font-size:12.5px;color:#666;line-height:16px;padding-bottom:10px;border-bottom:1px solid var(--rule)}
.news-item.last p{border-bottom:0}
.welcome{left:374px;top:575px;width:660px;height:229px;padding:12px 18px}
.welcome h2{font-size:29px;font-weight:400;color:#555;display:flex;align-items:center;gap:14px}
.welcome-dot{width:38px;height:38px;border-radius:50%;background:#9aa3ad}
.welcome p{font-size:12.7px;line-height:23.5px;letter-spacing:.35px;margin-top:12px;color:#555}
.welcome .btn{position:absolute;right:28px;bottom:13px}
.mini{top:833px;height:172px;padding:12px 20px}
.mini h2{font-size:24px;font-weight:400;color:#555;padding-bottom:6px;border-bottom:1px solid var(--rule);width:280px}
.what{left:374px;width:318px}
.what p{font-size:12.6px;line-height:18px;letter-spacing:1px;margin-top:9px}
.what .btn{position:absolute;left:19px;bottom:12px}
.news .btn{position:absolute;left:100px;bottom:28px}
.letter{left:718px;width:318px}
.letter p{font-size:12.6px;margin-top:5px;margin-left:-4px}
.email-field{margin:15px 0 0 -4px;width:209px;height:32px;border:1px solid #aaa;border-radius:3px;background:#fff;font-size:12px;color:#999;padding:8px}
.letter .btn{position:absolute;left:32px;bottom:12px}

/* footer */
.footer{left:0;top:1032px;width:1164px;height:168px;background:var(--blue);color:#fff}
.f-head{position:absolute;top:18px;font-size:20px;font-weight:500;padding-bottom:4px;border-bottom:1px dashed rgba(255,255,255,.6)}
.f-list{position:absolute;list-style:none;font-size:12.5px;line-height:16px}
.f-list li{margin-bottom:7px;padding-left:14px;position:relative}
.f-list li::before{content:"»";position:absolute;left:0;font-size:11px}
.f-divider{position:absolute;top:20px;width:1px;height:132px;background:rgba(255,255,255,.3)}
.contact{position:absolute;left:482px;top:54px;font-size:12.5px;line-height:17px}
.contact div{display:flex;gap:10px;margin-bottom:9px;align-items:flex-start}
.social{position:absolute;left:697px;top:56px;font-size:12.5px}
.social div{display:flex;align-items:center;gap:9px;margin-bottom:16px}
.social b{width:18px;height:18px;background:#fff;opacity:.85;border-radius:3px;display:block}
.f-brand{position:absolute;left:875px;top:22px;text-align:center;width:100px}
.f-brand-dot{width:96px;height:96px;border-radius:50%;border:3px solid #fff;margin:0 auto;display:flex;align-items:center;justify-content:center;font-size:15px;font-weight:500}
.copy{position:absolute;left:876px;top:122px;font-size:12.5px;line-height:15px}
</style>
</head>
<body>

<header>
  <div class="abs brand">
    <div class="brand-dot"></div>
    <div class="brand-name">BuddyScope</div>
    <div class="brand-tag">Next Generation Pathology Consultants</div>
  </div>
  <div class="abs account-links"><a href="#">Register</a><span>|</span><a href="#">Login</a></div>
  <div class="abs phone">
    <svg width="26" height="26" viewBox="0 0 24 24" aria-hidden="true"><path fill="#555" d="M6.6 10.8c1.4 2.8 3.8 5.1 6.6 6.6l2.2-2.2c.3-.3.7-.4 1-.2 1.1.4 2.3.6 3.6.6.6 0 1 .4 1 1V20c0 .6-.4 1-1 1C10.6 21 3 13.4 3 4c0-.6.4-1 1-1h3.5c.6 0 1 .4 1 1 0 1.3.2 2.5.6 3.6.1.3 0 .7-.2 1L6.6 10.8z"/></svg>
    123-456-7890
  </div>
  <a class="abs cta-order" href="#"><span>Order Services</span></a>
  <nav class="abs main-nav nav-row1"><a href="#">Check Report</a><i>|</i><a href="#">Set Up New Account</a><i>|</i><a href="#">Speak With One Of The Pathologists</a></nav>
  <nav class="abs main-nav nav-row2"><a href="#">See Our Test Menu</a><i>|</i><a href="#">Access Our Educational Material / Webinars</a></nav>
</header>

<section>
  <div class="abs hero" role="img" aria-label="Photo of a pathologist in a suit touching a transparent data screen with charts and a world map"></div>
  <div class="abs hero-panel"></div>
  <h1 class="abs hero-title" style="font-weight:400">Path<br>to the<br>Diagnosis</h1>
  <svg class="abs hero-arrow" style="left:100px" width="32" height="44" viewBox="0 0 32 44" aria-hidden="true"><path d="M26 4 L8 22 L26 40" fill="none" stroke="#1a6fb8" stroke-width="7"/></svg>
  <svg class="abs hero-arrow" style="left:1028px" width="32" height="44" viewBox="0 0 32 44" aria-hidden="true"><path d="M6 4 L24 22 L6 40" fill="none" stroke="#1a6fb8" stroke-width="7"/></svg>
</section>

<main>
  <aside class="abs card news">
    <div class="news-head">NEWS / BLOG</div>
    <div class="news-item" style="top:48px"><h3>Lorem Ipsum dummy</h3><span class="news-date">June 01, 2013</span><p>lorem ipsum is dummy text.<br>lorem</p></div>
    <div class="news-item" style="top:160px"><h3>Lorem Ipsum dummy</h3><span class="news-date">June 01, 2013</span><p>lorem ipsum is dummy text.</p></div>
    <div class="news-item last" style="top:263px"><h3>Lorem Ipsum dummy</h3><span class="news-date">June 01, 2013</span><p>lorem ipsum is dummy text.<br>lorem</p></div>
    <a class="btn" href="#">Read More <span>»</span></a>
  </aside>

  <article class="abs card welcome">
    <h2><span class="welcome-dot"></span>Welcome To BuddyScope</h2>
    <p>Lorem ipsum dolor sit amet, consectetuer adipiscing elit, sed diam nonummy nibh euismod tincidunt ut laoreet dolore magna aliquam erat volutpat. Ut wisi enim ad minim veniam, quis nostrud exerci tation ullamcorper suscipit lobortis nisl ut aliquip ex ea commodo consequat. Duis autem vel eum iriure dolor in hendrerit in vulputate velit esse molestie consequat, vel illum dolore eu feugiat nulla facilisis at vero eros et accumsan et iusto odio dignissim qui blandit praesent luptatum zzril delenit augue duis dolore te feugait nulla facilisi.hendrerit in vulputate velit esse molesti....</p>
    <a class="btn" href="#">Read More <span>»</span></a>
  </article>

  <section class="abs card mini what">
    <h2>What We Do</h2>
    <p>Lorem ipsum dolor sit amet, consectetuer adipiscing elit, sed diam nonummy nibh euismod tincidunt ut laoreet dolore magna...</p>
    <a class="btn" href="#">Read More <span>»</span></a>
  </section>

  <section class="abs card mini letter">
    <h2>Newsletter</h2>
    <p>Lorem ipsum dmaruiolor sit afdddamet</p>
    <div class="email-field">Enter your Email address</div>
    <a class="btn" href="#">Subscribe <span>»</span></a>
  </section>
</main>

<footer class="abs footer">
  <div class="f-head" style="left:125px">NAVIGATION</div>
  <ul class="f-list" style="left:129px;top:56px;width:140px">
    <li>Order Services</li><li>Check Results</li><li>Set Up New Account</li><li>Speak With One Of The Pathologists</li>
  </ul>
  <ul class="f-list" style="left:280px;top:56px;width:160px">
    <li>See Our Test Menu</li><li>Access Our Educational Material / Webinars</li>
  </ul>
  <div class="f-divider" style="left:449px"></div>

  <div class="f-head" style="left:485px">CONTACT US</div>
  <div class="contact">
    <div><svg width="12" height="14" viewBox="0 0 12 14" aria-hidden="true"><path fill="#fff" d="M6 0a5 5 0 0 0-5 5c0 4 5 9 5 9s5-5 5-9a5 5 0 0 0-5-5zm0 7a2 2 0 1 1 0-4 2 2 0 0 1 0 4z"/></svg><span>Lorem ipsum dolor sit<br>Vestibulum ac torto</span></div>
    <div><svg width="14" height="14" viewBox="0 0 24 24" aria-hidden="true"><path fill="#fff" d="M6.6 10.8c1.4 2.8 3.8 5.1 6.6 6.6l2.2-2.2c.3-.3.7-.4 1-.2 1.1.4 2.3.6 3.6.6.6 0 1 .4 1 1V20c0 .6-.4 1-1 1C10.6 21 3 13.4 3 4c0-.6.4-1 1-1h3.5c.6 0 1 .4 1 1 0 1.3.2 2.5.6 3.6.1.3 0 .7-.2 1z"/></svg><span>(123) 456-789</span></div>
    <div><svg width="14" height="14" viewBox="0 0 14 14" aria-hidden="true"><rect x="3" y="1" width="8" height="4" fill="none" stroke="#fff"/><rect x="1" y="5" width="12" height="6" rx="1" fill="#fff"/><rect x="3" y="9" width="8" height="4" fill="var(--blue)" stroke="#fff"/></svg><span>(0123) 456-789</span></div>
    <div><svg width="16" height="12" viewBox="0 0 16 12" aria-hidden="true"><rect x=".5" y=".5" width="15" height="11" fill="none" stroke="#fff"/><path d="M.5 .5 8 7l7.5-6.5" fill="none" stroke="#fff"/></svg><span>info@example.com</span></div>
  </div>
  <div class="f-divider" style="left:656px"></div>

  <div class="f-head" style="left:696px">FOLLOW US</div>
  <div class="social">
    <div><b></b>Friendline</div>
    <div><b></b>Chirpnet</div>
    <div><b></b>WorkLink</div>
  </div>
  <div class="f-divider" style="left:827px"></div>

  <div class="f-brand"><div class="f-brand-dot">BuddyScope</div></div>
  <div class="copy">© Copyright 2013 BuddyScope.<br>All rights reserved.</div>
</footer>

</body>
</html>
```